Flyer for the Lumen 2025 Conference

I am looking to produce a flyer for our upcoming conference, Lumen 2025. This is an annual conference that we plan to publicize on social media. The ideal designer will create a flyer that is eye-catching and effectively communicates the key information. Please see attached our logo, speaker photo, and flyer content.

Target Market(s)

All demographics

Industry/Entity Type

Christian

Font styles to use
Sans Serif

Requirements
Should not have
• Cross, church

```html
<!DOCTYPE html>
<html lang="en">
<head>
<meta charset="utf-8">
<title>Lumen 2025 Conference Flyer</title>
<link href="https://fonts.googleapis.com/css2?family=Michroma&family=Oswald:wght@500;600&family=Poppins:wght@400;500;600;700&display=swap" rel="stylesheet">
<style>
  :root{
    --navy-deep:#081a3a;
    --navy:#0c2a58;
    --navy-light:#15407e;
    --gold:#f5b81e;
    --gold-light:#ffd95a;
    --gold-dark:#d98c0a;
    --red:#e01b22;
    --red-dark:#9c0f14;
    --white:#ffffff;
    --sky:#2f9bf0;
  }
  *{margin:0;padding:0;box-sizing:border-box}
  html,body{width:993px;height:1200px;overflow:hidden;background:#d6d6d6}
  .flyer{
    position:relative;width:993px;height:1200px;overflow:hidden;
    background:radial-gradient(ellipse at 70% 40%, var(--navy-light) 0%, var(--navy) 45%, var(--navy-deep) 100%);
    font-family:'Poppins',sans-serif;color:var(--white);
  }
  .speaker-faded{
    position:absolute;left:0;top:40px;width:320px;height:280px;
    background:radial-gradient(ellipse at 55% 45%, rgba(80,110,160,.45), rgba(12,42,88,0) 70%);
  }
  .speaker-photo{
    position:absolute;left:0;top:491px;width:560px;height:709px;
    background:radial-gradient(ellipse at 45% 40%, #1f63c4 0%, #174c9a 40%, rgba(12,42,88,0) 78%);
  }
  .brand{
    position:absolute;right:88px;top:128px;display:flex;align-items:center;gap:14px;
    font-family:'Poppins',sans-serif;font-weight:500;font-size:66px;letter-spacing:2px;color:var(--white);
  }
  .brand-dot{width:26px;height:26px;border-radius:50%;background:var(--gold)}
  .title{
    position:absolute;left:84px;top:238px;width:860px;white-space:nowrap;
    font-family:'Michroma',sans-serif;font-weight:400;font-size:124px;line-height:1.1;letter-spacing:10px;
    background:linear-gradient(180deg,var(--gold-light) 0%,var(--gold) 55%,var(--gold-dark) 100%);
    -webkit-background-clip:text;background-clip:text;color:transparent;
    -webkit-text-stroke:4px var(--gold);
  }
  .year{
    position:absolute;left:84px;top:376px;
    font-family:'Oswald',sans-serif;font-weight:600;font-size:92px;line-height:1.1;
    color:#e9edf3;
  }
  .banner{
    position:absolute;left:298px;top:380px;width:642px;height:104px;
    background:linear-gradient(90deg,var(--red-dark),var(--red));
    display:flex;align-items:center;justify-content:center;white-space:nowrap;
    font-family:'Oswald',sans-serif;font-weight:600;font-size:56px;line-height:1;letter-spacing:0;
  }
  .topic{
    position:absolute;left:366px;top:525px;width:570px;height:44px;
    border:1px solid rgba(255,255,255,.35);border-radius:6px;display:flex;align-items:center;
  }
  .topic-label{
    height:100%;width:118px;background:var(--gold);color:var(--navy-deep);border-radius:5px;
    font-weight:700;font-size:30px;display:flex;align-items:center;justify-content:center;
  }
  .topic-text{padding-left:18px;font-weight:500;font-size:33px;white-space:nowrap}
  .dates{position:absolute;left:415px;top:605px;display:flex;gap:8px}
  .date-card{width:170px;height:115px;border-radius:8px;overflow:hidden;background:var(--navy-deep);
    display:flex;flex-direction:column;box-shadow:0 0 0 1px rgba(255,255,255,.15)}
  .date-day{height:32px;background:var(--gold);color:var(--navy-deep);white-space:nowrap;
    font-family:'Oswald',sans-serif;font-weight:500;font-size:18px;display:flex;align-items:center;justify-content:center}
  .date-num{flex:1;display:flex;align-items:center;justify-content:center;
    font-family:'Michroma',sans-serif;font-size:38px;-webkit-text-stroke:1.5px var(--white)}
  .date-num sup{font-size:22px;margin-top:-16px}
  .date-time{height:32px;background:linear-gradient(90deg,var(--red-dark),var(--red));white-space:nowrap;
    font-family:'Oswald',sans-serif;font-weight:500;font-size:20px;display:flex;align-items:center;justify-content:center}
  .venue{position:absolute;left:415px;top:755px;display:flex;gap:22px}
  .venue-name{font-family:'Oswald',sans-serif;font-weight:500;font-size:25px;color:var(--sky);line-height:1.2;white-space:nowrap}
  .venue-address{font-size:20px;line-height:1.3;font-weight:500}
  .app-band{
    position:absolute;left:375px;top:868px;width:618px;height:96px;
    background:linear-gradient(90deg,rgba(30,80,150,.0),rgba(30,80,150,.85) 20%,rgba(30,80,150,.85) 80%,rgba(30,80,150,0));
  }
  .app-text{position:absolute;left:420px;top:880px;width:420px;text-align:center}
  .app-title{font-weight:600;font-size:24px;white-space:nowrap}
  .app-title span{color:var(--gold)}
  .app-sub{font-size:21px;color:#dfe6f2;white-space:nowrap}
  .app-phone{position:absolute;left:839px;top:833px;width:76px;height:147px;border-radius:10px;
    background:linear-gradient(180deg,#ffffff,#dfe6f2);border:3px solid #111}
  .contacts{position:absolute;left:588px;top:1008px;list-style:none}
  .contacts li{display:flex;align-items:center;gap:14px;margin-bottom:6px;white-space:nowrap}
  .contact-phone{font-weight:600;font-size:40px}
  .contact-line{font-size:27px;font-weight:500}
  .icon{width:24px;height:24px;flex:none}
  .speaker-label{position:absolute;left:86px;top:1046px;font-size:34px;font-weight:500}
  .speaker-name{position:absolute;left:86px;top:1088px;white-space:nowrap;font-family:'Oswald',sans-serif;font-weight:500;font-size:48px;color:var(--gold)}
</style>
</head>
<body>
<main class="flyer">
  <div class="speaker-faded" role="img" aria-label="Faded portrait of the speaker"></div>
  <div class="speaker-photo" role="img" aria-label="Speaker seated in a blue suit"></div>

  <div class="brand"><span class="brand-dot"></span>KAVEL</div>

  <h1 class="title">LUMEN</h1>
  <div class="year">2025</div>
  <div class="banner">A PROPHETIC CONFERENCE</div>

  <div class="topic"><span class="topic-label">TOPIC</span><span class="topic-text">The Voice Of The Lord</span></div>

  <div class="dates">
    <div class="date-card"><div class="date-day">FRIDAY, DECEMBER</div><div class="date-num">26<sup>TH</sup></div><div class="date-time">6:30PM - 9:00PM</div></div>
    <div class="date-card"><div class="date-day">SATURDAY, DECEMBER</div><div class="date-num">27<sup>TH</sup></div><div class="date-time">5:30PM - 8:00PM</div></div>
    <div class="date-card"><div class="date-day">SUNDAY, DECEMBER</div><div class="date-num">29<sup>TH</sup></div><div class="date-time">4:30PM - 7:00PM</div></div>
  </div>

  <div class="venue">
    <svg width="50" height="56" viewBox="0 0 50 56" aria-hidden="true">
      <ellipse cx="25" cy="50" rx="20" ry="5" fill="none" stroke="#e01b22" stroke-width="3"/>
      <path d="M25 2C15 2 8 9 8 18c0 12 17 30 17 30s17-18 17-30C42 9 35 2 25 2z" fill="#e01b22"/>
      <circle cx="25" cy="18" r="6" fill="#0c2a58"/>
    </svg>
    <div>
      <div class="venue-name">THE RIVERSIDE PERFORMING ARTS CENTER</div>
      <div class="venue-address">128 Maplewood Avenue Riverside,<br>Maine 04000</div>
    </div>
  </div>

  <div class="app-band"></div>
  <div class="app-text">
    <div class="app-title">Download the <span>KAVEL App</span></div>
    <div class="app-sub">to stay updated on the event</div>
  </div>
  <div class="app-phone" role="img" aria-label="Phone showing the event app screen"></div>

  <ul class="contacts">
    <li><svg class="icon" viewBox="0 0 24 24" aria-hidden="true"><circle cx="12" cy="12" r="12" fill="#f5b81e"/><path d="M8 6l2 0 1 3-1.5 1a7 7 0 003.5 3.5l1-1.5 3 1v2c0 1-1 2-2 2A10 10 0 016 8c0-1 1-2 2-2z" fill="#0c2a58"/></svg><span class="contact-phone">207 555 0142</span></li>
    <li><svg class="icon" viewBox="0 0 24 24" aria-hidden="true"><circle cx="12" cy="12" r="12" fill="#f5b81e"/><rect x="6" y="8" width="12" height="8" rx="1" fill="#0c2a58"/><path d="M6 8l6 5 6-5" stroke="#f5b81e" fill="none"/></svg><span class="contact-line">contact@kavel.org</span></li>
    <li><svg class="icon" viewBox="0 0 24 24" aria-hidden="true"><circle cx="12" cy="12" r="12" fill="#f5b81e"/><g fill="none" stroke="#0c2a58" stroke-width="1.4"><circle cx="12" cy="12" r="6"/><ellipse cx="12" cy="12" rx="2.5" ry="6"/><path d="M6 12h12"/></g></svg><span class="contact-line">www.kavel.org</span></li>
  </ul>

  <div class="speaker-label">SPEAKER</div>
  <div class="speaker-name">PROPHET SAMUEL ADEYO</div>
</main>
</body>
</html>
```